Hamper box design

We are a chocolate business and need a sophisticated, premium hamper box design. Our hamper box is black and we tie a ribbon on the outside (please see attached photo).

Requirements:
- Incorporate our logo or picture of bean on the top surface of the hamper box
- Need a design for the inside of the top lid (see attachment "Inside Design" for an example)

The dimensions of the actual hamper boxes (need the correct files for these sizes):
1. 240mm wide x 210mm long x 60mm deep.
2. 340mm wide x 260mm long x 90mm deep.
3. 420mm wide x 330mm long x 110mm deep.

Suggestions (not essential):
- Where Chocolate Meets Craftmanship (our slogan)
- The smoothest French chocolate experience
- A thin gold border styling on the top and/or inside surface (to give sophisticated feel) See "Tobias Wrenfield border" file
- Follow us:
(instagram symbol) @brindlewoodtreats
(facebook symbol) facebook.com/brindlewoodtreats
(world symbol) www.brindlewoodtreats.com.au

Our website is: www.brindlewoodtreats.com.au
Potential inspiration from our instagram.com/brindlewoodtreats

```html
<!DOCTYPE html>
<html lang="en">
<head>
<meta charset="utf-8">
<title>Brindlewood Treats – Hamper Box Lid</title>
<link rel="stylesheet" href="https://fonts.googleapis.com/css2?family=Josefin+Sans:wght@400;600&family=Open+Sans:wght@400&display=swap">
<style>
  :root {
    --page: #ffffff;
    --ink: #000000;
    --board: #050607;
    --gold: #b07a3e;
    --gold-light: #d9a95c;
    --gold-deep: #6e4420;
  }
  * { box-sizing: border-box; margin: 0; padding: 0; }
  html, body { width: 1200px; height: 2565px; overflow: hidden; background: var(--page); }
  .sheet { position: relative; width: 1200px; height: 2565px; }

  .face-label {
    position: absolute; left: 0; width: 1200px; text-align: center;
    font-family: "Open Sans", sans-serif; font-weight: 400;
    font-size: 176px; line-height: 1; color: var(--ink);
  }
  .face-label--outer { top: 62px; }
  .face-label--inner { top: 1318px; }

  .lid {
    position: absolute; left: 65px; width: 1070px; height: 936px;
    background: var(--board); overflow: hidden;
  }
  .lid--outer { top: 324px; }
  .lid--inner { top: 1552px; }

  .lid-frame { position: absolute; inset: 0; width: 1070px; height: 936px; }

  .gold-sweep { position: absolute; left: 0; width: 1070px; }
  .lid--outer .gold-sweep {
    top: 250px; height: 580px;
    background:
      radial-gradient(ellipse 60% 30% at 70% 55%, rgba(217,169,92,.55), transparent 70%),
      radial-gradient(ellipse 45% 28% at 20% 45%, rgba(176,122,62,.45), transparent 70%),
      linear-gradient(175deg, transparent 25%, rgba(176,122,62,.28) 50%, transparent 75%);
  }
  .lid--inner .gold-sweep {
    top: 600px; height: 336px;
    background:
      radial-gradient(ellipse 60% 40% at 75% 50%, rgba(217,169,92,.55), transparent 70%),
      radial-gradient(ellipse 45% 40% at 20% 60%, rgba(176,122,62,.45), transparent 70%),
      linear-gradient(170deg, transparent 15%, rgba(176,122,62,.3) 55%, transparent 90%);
  }

  .brand {
    position: absolute; left: 0; width: 1070px; text-align: center;
    font-family: "Josefin Sans", sans-serif; font-weight: 400; color: var(--gold);
  }
  .brand-name { font-size: 82px; letter-spacing: 6px; line-height: 1; }
  .brand-sub { font-size: 44px; letter-spacing: 22px; margin-top: 26px; padding-left: 22px; line-height: 1; }
  .lid--outer .brand { top: 262px; }
  .lid--inner .brand { top: 250px; }

  .tagline {
    position: absolute; left: 0; width: 1070px; text-align: center;
    font-family: "Josefin Sans", sans-serif; font-weight: 600; color: var(--gold);
  }
  .lid--outer .tagline { top: 776px; font-size: 28px; }
  .lid--inner .tagline { top: 479px; font-size: 24px; }

  .divider { position: absolute; left: 318px; width: 434px; height: 14px; }
  .divider--top { top: 450px; }
  .divider--bottom { top: 522px; }

  .follow {
    position: absolute; left: 0; width: 1070px; text-align: center;
    font-family: "Josefin Sans", sans-serif; font-weight: 400; font-size: 19px;
    color: var(--gold); line-height: 1;
  }
  .follow-row { display: flex; justify-content: center; align-items: center; gap: 10px; }
  .follow-row + .follow-row { margin-top: 12px; }
  .follow-item { display: inline-flex; align-items: center; gap: 7px; }
  .follow-item + .follow-item { margin-left: 10px; }
  .follow-dot { width: 17px; height: 17px; border: 1.5px solid var(--gold); border-radius: 50%; display: inline-block; }
  .follow-globe { width: 18px; height: 18px; }
  .lid--inner .follow { top: 584px; }
</style>
</head>
<body>
<div class="sheet">

  <div class="face-label face-label--outer">Outer</div>

  <section class="lid lid--outer">
    <div class="gold-sweep" role="img" aria-label="Flowing gold particle wave ribbons sweeping across the lid"></div>
    <svg class="lid-frame" viewBox="0 0 1070 936" aria-hidden="true">
      <defs>
        <linearGradient id="rule-h" x1="0" x2="1">
          <stop offset="0" stop-color="#b07a3e" stop-opacity="0"/>
          <stop offset=".5" stop-color="#b07a3e"/>
          <stop offset="1" stop-color="#b07a3e" stop-opacity="0"/>
        </linearGradient>
        <linearGradient id="rule-v" x1="0" x2="0" y1="0" y2="1">
          <stop offset="0" stop-color="#8a5a2c" stop-opacity="0"/>
          <stop offset=".5" stop-color="#8a5a2c"/>
          <stop offset="1" stop-color="#8a5a2c" stop-opacity="0"/>
        </linearGradient>
      </defs>
      <rect x="79" y="63" width="906" height="3" fill="url(#rule-h)"/>
      <rect x="79" y="868" width="906" height="3" fill="url(#rule-h)"/>
      <rect x="79" y="60" width="3" height="860" fill="url(#rule-v)"/>
      <rect x="985" y="60" width="3" height="860" fill="url(#rule-v)"/>
    </svg>
    <div class="brand">
      <div class="brand-name">Brindlewood</div>
      <div class="brand-sub">TREATS</div>
    </div>
    <p class="tagline">Where Chocolate Meets Craftmanship</p>
  </section>

  <div class="face-label face-label--inner">inner</div>

  <section class="lid lid--inner">
    <div class="gold-sweep" role="img" aria-label="Flowing gold particle wave ribbons across the lower edge"></div>
    <svg class="lid-frame" viewBox="0 0 1070 936" aria-hidden="true">
      <defs>
        <linearGradient id="rule-h2" x1="0" x2="1">
          <stop offset="0" stop-color="#b07a3e" stop-opacity="0"/>
          <stop offset=".5" stop-color="#b07a3e"/>
          <stop offset="1" stop-color="#b07a3e" stop-opacity="0"/>
        </linearGradient>
        <linearGradient id="rule-v2" x1="0" x2="0" y1="0" y2="1">
          <stop offset="0" stop-color="#8a5a2c" stop-opacity="0"/>
          <stop offset=".5" stop-color="#8a5a2c"/>
          <stop offset="1" stop-color="#8a5a2c" stop-opacity="0"/>
        </linearGradient>
      </defs>
      <rect x="79" y="65" width="906" height="3" fill="url(#rule-h2)"/>
      <rect x="79" y="60" width="3" height="860" fill="url(#rule-v2)"/>
      <rect x="985" y="60" width="3" height="860" fill="url(#rule-v2)"/>
    </svg>
    <div class="brand">
      <div class="brand-name">Brindlewood</div>
      <div class="brand-sub">TREATS</div>
    </div>

    <svg class="divider divider--top" viewBox="0 0 434 14" aria-hidden="true">
      <line x1="6" y1="7" x2="428" y2="7" stroke="#b07a3e" stroke-width="2"/>
      <path d="M0 7 6 2 12 7 6 12Z M211 7 217 1 223 7 217 13Z M422 7 428 2 434 7 428 12Z" fill="#b07a3e"/>
    </svg>
    <p class="tagline">The smoothest French chocolate experience</p>
    <svg class="divider divider--bottom" viewBox="0 0 434 14" aria-hidden="true">
      <line x1="6" y1="7" x2="428" y2="7" stroke="#b07a3e" stroke-width="2"/>
      <path d="M0 7 6 2 12 7 6 12Z M211 7 217 1 223 7 217 13Z M422 7 428 2 434 7 428 12Z" fill="#b07a3e"/>
    </svg>

    <div class="follow">
      <div class="follow-row">
        <span class="follow-item"><span class="follow-dot"></span>@brindlewoodtreats</span>
        <span class="follow-item"><span class="follow-dot"></span>brindlewoodtreats</span>
      </div>
      <div class="follow-row">
        <span class="follow-item">
          <svg class="follow-globe" viewBox="0 0 18 18" aria-hidden="true" fill="none" stroke="#b07a3e" stroke-width="1.3">
            <circle cx="9" cy="9" r="7.5"/>
            <ellipse cx="9" cy="9" rx="3.3" ry="7.5"/>
            <line x1="1.5" y1="9" x2="16.5" y2="9"/>
            <line x1="3" y1="5" x2="15" y2="5"/>
            <line x1="3" y1="13" x2="15" y2="13"/>
          </svg>
          www.brindlewoodtreats.com.au
        </span>
      </div>
    </div>
  </section>

</div>
</body>
</html>
```